Business Card Design Project

In addition to the logo design we want a professional and contemporary business card for a talent management agency. We provide management services to creative artists and want to communicate a professional creative vibe.
Updates

Project Deadline Extended
Reason: Sorry didnt realise I had put such a short timeline on it.

Target Market(s)

The business deals with creative artists and other industry professionals

Industry/Entity Type

Artists

Colors

Designer to choose colors to be used in the design.

Requirements
Must have
• Logo
Address
Phone
Email

```html
<!DOCTYPE html>
<html lang="en">
<head>
<meta charset="utf-8">
<title>Kestrel Talent — Business Card</title>
<link href="https://fonts.googleapis.com/css2?family=Arimo:wght@400;700&display=swap" rel="stylesheet">
<style>
  :root {
    --backdrop: #e9e7e3;
    --card-white: #ffffff;
    --brand-green: #1d5b37;
    --ink-light: #ffffff;
    --ink-soft: rgba(255,255,255,0.88);
  }
  * { margin: 0; padding: 0; box-sizing: border-box; }
  html, body {
    width: 1200px; height: 960px; overflow: hidden;
    background: var(--backdrop);
    font-family: "Arimo", Arial, sans-serif;
  }
  .stage {
    position: relative; width: 1200px; height: 960px;
    display: flex; justify-content: center; align-items: center; gap: 90px;
  }
  .card {
    position: relative; width: 330px; height: 540px;
    border-radius: 18px;
    box-shadow: 0 6px 18px rgba(0,0,0,0.16);
  }
  .card--front { background: var(--card-white); }
  .card--back { background: var(--brand-green); color: var(--ink-light); }

  .wordmark {
    position: absolute; left: 28px;
    font-weight: 700; font-size: 30px; line-height: 1;
    letter-spacing: 0.5px;
  }
  .card--front .wordmark { bottom: 48px; color: var(--brand-green); }
  .card--back .wordmark { top: 250px; color: var(--ink-light); }

  .contact { position: absolute; left: 28px; top: 300px; right: 24px; }
  .contact__name { font-weight: 700; font-size: 20px; line-height: 1.1; }
  .contact__role { font-size: 13px; color: var(--ink-soft); margin-top: 2px; }
  .contact__list { list-style: none; margin-top: 22px; font-size: 13px; line-height: 1.45; color: var(--ink-soft); }
  .contact__item { display: flex; align-items: center; gap: 8px; }
  .contact__item svg { width: 12px; height: 12px; flex: none; fill: var(--ink-light); }
  .contact__address { margin-top: 2px; }
</style>
</head>
<body>
<main class="stage">
  <section class="card card--front" aria-label="Card front">
    <div class="wordmark">Kestrel Talent</div>
  </section>

  <section class="card card--back" aria-label="Card back">
    <div class="wordmark">Kestrel Talent</div>
    <div class="contact">
      <p class="contact__name">Employee Name</p>
      <p class="contact__role">Managing Director</p>
      <ul class="contact__list">
        <li class="contact__item">
          <svg viewBox="0 0 12 12" aria-hidden="true"><circle cx="6" cy="3.5" r="2.6"/><path d="M0.8 12c0-3 2.3-5 5.2-5s5.2 2 5.2 5z"/></svg>
          (+61 2) 5550 1742
        </li>
        <li class="contact__item">
          <svg viewBox="0 0 12 12" aria-hidden="true"><path d="M0.5 2.5h11v7h-11z"/><path d="M0.5 2.5l5.5 4 5.5-4" fill="none" stroke="#1d5b37" stroke-width="1"/></svg>
          hello@kestrel.com.au
        </li>
        <li class="contact__address">27 Wattle Row, Glenmore NSW 2090<br>Australia</li>
      </ul>
    </div>
  </section>
</main>
</body>
</html>
```